Www.vexorlane.com monthly sweepstakes.

Every month I am giving away 1st place $500 gift card to your local RC hobby shop of choice, 2nd place $100 gift card 3rd place Vexorlane merch. All things rc: cars, boats, quadcopters, helicopters, airplanes.

Needs to be with the color theme of the website. Check vexorlane.com for current sweepstakes banner. New banner should be half the size in height. I will post dimension later.

Target Market(s)

Rc hobbies cars airplanes helicopters boats

Industry/Entity Type

RemoteControl hobbies

Requirements
Must have
• 1440x680 size, Blend with black background, creative and in incorporate all trypes of rc craft
Should not have
• To many different colors, dosnt need logo as its already on website. This is a banner for my homepage

```html
<!DOCTYPE html>
<html lang="en">
<head>
<meta charset="utf-8">
<title>Vexorlane Monthly Sweepstakes</title>
<link href="https://fonts.googleapis.com/css2?family=Montserrat:ital,wght@1,800;1,900&family=Open+Sans:wght@400;700&display=swap" rel="stylesheet">
<style>
  :root {
    --bg-core: #3d0a0d;
    --bg-edge: #140304;
    --headline-top: #fff6b0;
    --headline-mid: #ffd21a;
    --headline-low: #ffb300;
    --extrude: #d10a0a;
    --extrude-deep: #8e0303;
    --ghost: rgba(150, 20, 24, 0.55);
    --band-red: #c40c10;
    --prize-orange: #ffa200;
    --prize-ink: #a50d0d;
    --white: #ffffff;
  }
  * { box-sizing: border-box; margin: 0; padding: 0; }
  html, body {
    width: 1200px; height: 567px; overflow: hidden; background: #000;
  }
  .banner {
    position: relative; width: 1200px; height: 567px; overflow: hidden;
    background: radial-gradient(ellipse 75% 80% at 50% 45%, var(--bg-core) 0%, #2a0709 55%, var(--bg-edge) 100%);
    font-family: "Open Sans", Arial, sans-serif;
  }

  /* craft imagery areas */
  .craft { position: absolute; }
  .craft--helicopter {
    left: -10px; top: 10px; width: 280px; height: 160px;
    border-radius: 45% 55% 40% 50%;
    background: linear-gradient(160deg, #e8242a 0%, #b3101a 60%, #5a0a0d 100%);
    transform: rotate(-14deg);
  }
  .craft--airplane {
    left: 930px; top: -10px; width: 275px; height: 255px;
    border-radius: 40% 10% 45% 55%;
    background: linear-gradient(200deg, #f04a4a 0%, #d21b22 50%, #6d0d10 100%);
  }
  .craft--boat {
    left: -10px; top: 395px; width: 325px; height: 150px;
    border-radius: 20% 60% 45% 25%;
    background: linear-gradient(170deg, #2a3a7a 0%, #d8242a 45%, #e85a40 70%, #5a0a0d 100%);
    transform: rotate(14deg);
  }
  .craft--truck {
    left: 885px; top: 300px; width: 330px; height: 280px;
    border-radius: 35% 20% 10% 40%;
    background: linear-gradient(165deg, #e42a2a 0%, #b4141a 40%, #2a2a2e 75%, #121214 100%);
  }

  /* headline */
  .headline {
    position: absolute; left: 0; top: 0; width: 1200px; height: 340px;
    font-family: "Montserrat", Arial, sans-serif; font-style: italic; font-weight: 900;
  }
  .headline text { font-size: 118px; }

  /* category band */
  .category-band {
    position: absolute; left: 280px; top: 343px; width: 620px; height: 31px;
    background: var(--band-red); border-radius: 6px;
    color: var(--white); font-size: 16.6px; line-height: 31px;
    padding-left: 22px; white-space: nowrap;
  }
  .category-band strong { font-weight: 700; }

  /* prizes */
  .prize {
    position: absolute; top: 403px; width: 178px; height: 99px;
    background: var(--prize-orange);
    border: 3px solid var(--white); border-radius: 20px;
    transform: skewX(-10deg);
    color: var(--prize-ink);
  }
  .prize__inner { position: absolute; inset: 0; transform: skewX(10deg); }
  .prize--first { left: 326px; }
  .prize--second { left: 512px; }
  .prize--third { left: 697px; }
  .prize__rank {
    position: absolute; left: 18px; top: 16px;
    font-size: 52px; line-height: 52px; font-weight: 400;
  }
  .prize__suffix {
    position: absolute; left: 46px; top: 20px; font-size: 13px; line-height: 13px;
  }
  .prize__label {
    position: absolute; left: 20px; top: 69px; font-size: 10px; line-height: 12px;
  }
  .prize__detail {
    position: absolute; left: 74px; top: 16px; width: 80px;
    font-size: 10.5px; line-height: 14px;
  }
  .prize--second .prize__detail { left: 82px; width: 90px; }
  .prize--third .prize__detail { left: 86px; width: 90px; }
  .prize--second .prize__suffix,
  .prize--third .prize__suffix { left: 50px; }
</style>
</head>
<body>
<main class="banner">
  <div class="craft craft--helicopter" role="img" aria-label="Red RC helicopter"></div>
  <div class="craft craft--airplane" role="img" aria-label="Red RC airplane with large wheels"></div>
  <div class="craft craft--boat" role="img" aria-label="Red and blue RC racing catamaran boat"></div>
  <div class="craft craft--truck" role="img" aria-label="Red and black RC short course truck"></div>

  <svg class="headline" viewBox="0 0 1200 340" aria-label="Every month I am giving away">
    <defs>
      <linearGradient id="headlineFill" x1="0" y1="0" x2="0" y2="1">
        <stop offset="0" stop-color="#fff6b0"/>
        <stop offset="0.45" stop-color="#ffd21a"/>
        <stop offset="1" stop-color="#ffb300"/>
      </linearGradient>
      <text id="lineOne" x="237" y="180" textLength="690" lengthAdjust="spacingAndGlyphs">EVERY MONTH</text>
      <text id="lineTwo" x="142" y="290" textLength="935" lengthAdjust="spacingAndGlyphs">I AM GIVING AWAY</text>
    </defs>
    <g transform="rotate(-3 600 230)">
      <g fill="var(--ghost)">
        <use href="#lineOne" x="-22" y="40"/>
        <use href="#lineTwo" x="-22" y="40"/>
      </g>
      <g fill="var(--extrude-deep)">
        <use href="#lineOne" x="-12" y="14"/>
        <use href="#lineTwo" x="-12" y="14"/>
      </g>
      <g fill="var(--extrude)">
        <use href="#lineOne" x="-10" y="11"/><use href="#lineTwo" x="-10" y="11"/>
        <use href="#lineOne" x="-8" y="9"/><use href="#lineTwo" x="-8" y="9"/>
        <use href="#lineOne" x="-6" y="7"/><use href="#lineTwo" x="-6" y="7"/>
        <use href="#lineOne" x="-4" y="4"/><use href="#lineTwo" x="-4" y="4"/>
        <use href="#lineOne" x="-2" y="2"/><use href="#lineTwo" x="-2" y="2"/>
      </g>
      <g fill="#fff1b8">
        <use href="#lineOne" x="-1" y="-1"/>
        <use href="#lineTwo" x="-1" y="-1"/>
      </g>
      <g fill="url(#headlineFill)">
        <use href="#lineOne"/>
        <use href="#lineTwo"/>
      </g>
    </g>
  </svg>

  <p class="category-band"><strong>ALL THINGS RC:</strong> CARS, BOATS, QUADCOPTERS, HELICOPTERS, AIRPLANES.</p>

  <section class="prize prize--first">
    <div class="prize__inner">
      <span class="prize__rank">1</span><span class="prize__suffix">ST</span>
      <span class="prize__label">PLACE</span>
      <p class="prize__detail">$500 Gift Card to your local RC hobby shop of choice.</p>
    </div>
  </section>
  <section class="prize prize--second">
    <div class="prize__inner">
      <span class="prize__rank">2</span><span class="prize__suffix">ND</span>
      <span class="prize__label">PLACE</span>
      <p class="prize__detail">$100 Gift Card</p>
    </div>
  </section>
  <section class="prize prize--third">
    <div class="prize__inner">
      <span class="prize__rank">3</span><span class="prize__suffix">RD</span>
      <span class="prize__label">PLACE</span>
      <p class="prize__detail">Vexorlane Merch</p>
    </div>
  </section>
</main>
</body>
</html>
```